Webdesign für ambulanten Intensivpflegedienst
Zielgruppe
Moin liebe Designer,
vorab einen guten Start ins neue Jahr :) Wir sind ein ambulanter Intensivpflegedienst im Speckgürtel Hamburgs. Wir betreuen seit über 20 Jahren Kinder, Jugendliche und Erwachsene, die eine dauerhafte Überwachung und Betreuung benötigen. Dabei sind unsere Pflegefachkräfte dauerhaft vor Ort. Wir haben kaum Fluktuation, eine hohe Mitarbeiterzufriedenheit und erhalten auch weiterhin Bewerbungen in diesem hart umkämpften Markt, leider ist es uns noch nicht gelungen diese positiven Aspekte öffentlichkeitswirksam nach außen zu tragen.
Aufgabenstellung
Neues Corporate Identity Design für eine Wordpress oder Joomla Seite.
Bilder können gerne aus bildmarktplatz-ost.com oder ähnlichen Marktplätzen vorgeschlagen werden. Dabei bitten wir auf Bilder mit älteren Menschen im Rollstuhl oder Pflegekräfte in Dienstkleidung zu verzichten, da unsere Mitarbeitenden unseren Kund:innen nicht das Bild einer Intensivstation vermitteln wollen, sondern ein würdiges Leben daheim oder unterwegs. Ebenso nutzen unsere Kund:innen Elektro-Rollstühle, sind mobil, gehen zur Schule oder in die Uni.
Gerne kann auch die Geschichte oder Bilder eines Betroffenen benutzt werden. Einige unserer Kund:innen spielen E-Rolli-Fußball: https://www.sportverband-muster.de/nachhaltigkeitsmanagement/news/news-detail/?tx_news_pi1%5Bnews%5D=648213 oder engagieren sich für benachteiligte.
Ein Gesichtsbuchs oder Bildfluss Account besteht nicht. Ein Nerv und KarriereNetz Profil sind im Aufbau.
Wir haben uns ein paar Websites angesehen, die auch unseren Wünschen entsprechen, diese können wir gerne auf Anfrage verschicken. Als Referenz unsere alte Website: https://seitenspeicher-beispiel.org/web/20190107114418/https://taleb-pflegedienst.de/ oder unsere aktuellen Stellenanzeigen: https://www.inseratbrett-muster.de/s-bestandsliste.html?userId=71564820
Als Thema/Farbkonzept für unsere Website würden wir gerne die Nähe zur Lüneburger Heide nutzen und auch in diesem Stil/ Farben etc. die Website gestalten. Beispielhaft kann dafür die Tourismusseite der Lüneburger Heide genommen werden: https://www.gruenland-ferien-beispiel.de/natur
Ersichtlich sind unsere Stellenanzeigen in blau gehalten und eher dem Wasser zugeneigt, wie auch unser Logo aus einem Fisch besteht und unsere alte Website eher an den ländlichen Raum. Da wir Kunden sowohl in Hamburg als auch in Schleswig-Holstein und zuletzt überwiegend in Niedersachsen (Lüneburger Heide) betreuen, würden wir uns freuen, wenn die Nähe zum Wasser und der Heide vereint werden kann.
Wir haben hier be..

```html
<!DOCTYPE html>
<html lang="de">
<head>
<meta charset="utf-8">
<title>Taleb Pflegedienst – Webdesign</title>
<link href="https://fonts.googleapis.com/css2?family=Roboto:wght@400;500;700&family=Roboto+Condensed:wght@300;400;700&display=swap" rel="stylesheet">
<style>
:root{
  --bg:#eef3f7;
  --blue:#2aa6e6;
  --blue-light:#5cc8f6;
  --blue-pale:#e3f3fc;
  --blue-deep:#1b6aa3;
  --sea-a:#7fc3e6;
  --sea-b:#1f6fa8;
  --pink:#e293d8;
  --purple:#8b2f7e;
  --ink:#1d1d1d;
  --grey:#7a7a7a;
  --white:#ffffff;
  --heath-a:#b9a0d3;
  --heath-b:#5f8a3e;
  --dark:#2b2b2b;
}
*{box-sizing:border-box;margin:0;padding:0}
html,body{width:1036px;height:1200px;overflow:hidden;background:var(--bg);font-family:"Roboto",Arial,sans-serif;color:var(--ink)}
.stage{position:absolute;left:267px;top:8px;width:851px;height:2007px;transform:scale(.59);transform-origin:0 0}
.page{position:absolute;top:0;width:444px;background:var(--white);overflow:hidden;box-shadow:0 6px 24px rgba(0,0,0,.25)}
.page--home{left:0;height:2007px;z-index:2}
.page--services{left:406px;top:187px;width:445px;height:1723px;z-index:1}
.abs{position:absolute}
.header{position:absolute;left:0;top:0;width:100%;height:52px;background:var(--white)}
.brand{position:absolute;font-family:"Roboto",sans-serif;font-weight:700;font-size:10px;color:var(--ink);display:flex;align-items:center;gap:4px}
.brand i{display:inline-block;width:8px;height:8px;border-radius:50%;background:var(--blue)}
.nav{position:absolute;top:22px;display:flex;gap:16px;font-size:6px;font-weight:500}
.nav-cta{position:absolute;top:0;height:52px;background:var(--blue);color:var(--white);font-size:6px;font-weight:700;display:flex;align-items:center;justify-content:flex-end;padding-right:24px;clip-path:polygon(30% 0,100% 0,100% 100%,0 100%)}
.hero{position:absolute;left:0;top:52px;width:100%;height:198px;background:linear-gradient(180deg,var(--sea-a),var(--sea-b))}
.hero-photo{position:absolute;inset:0;clip-path:polygon(88% 0,100% 0,100% 100%,55% 100%);}
.hero-stripe{position:absolute;inset:0;background:var(--blue-light);clip-path:polygon(86% 0,89% 0,56% 100%,52% 100%)}
.hero h1{position:absolute;left:28px;font-family:"Roboto",sans-serif;font-weight:700;font-size:17px;color:var(--white);letter-spacing:.2px}
.hero h2{position:absolute;left:28px;font-family:"Roboto Condensed",sans-serif;font-weight:300;font-size:18px;line-height:21px;color:var(--white)}
.band{position:absolute;left:0;width:100%;background:linear-gradient(90deg,var(--pink),var(--purple));color:var(--white);text-align:center}
.band h3{font-size:13px;font-weight:700;margin-top:20px}
.rule{width:22px;height:1px;background:var(--white);margin:7px auto}
.small{font-size:4.2px;line-height:6.5px;color:var(--grey)}
.band .small{color:#f6e3f3;width:190px;margin:0 auto}
.card{position:absolute;background:var(--white);border-radius:5px;box-shadow:0 2px 6px rgba(0,0,0,.22);text-align:center;padding:10px 8px 0}
.card b{display:block;font-size:7px;margin-bottom:6px}
.card .small{width:80px;margin:0 auto}
.icon{display:block;margin:0 auto 6px}
.eyebrow{font-size:4px;color:var(--blue);text-transform:uppercase;letter-spacing:.3px}
.eyebrow--pink{color:var(--pink)}
.h4{font-size:13px;font-weight:500;margin:2px 0 8px}
.btn{position:absolute;height:9px;padding:0 10px;border-radius:5px;background:var(--blue);color:var(--white);font-size:4.5px;font-weight:700;display:flex;align-items:center;box-shadow:0 2px 3px rgba(0,0,0,.2)}
.photo{position:absolute;border:2px solid var(--white);border-radius:5px;box-shadow:0 2px 6px rgba(0,0,0,.3)}
.ph-heath{background:linear-gradient(160deg,#e6a46b,#7a5b8c 55%,#4b6b3a)}
.ph-team{background:linear-gradient(160deg,#d9d4cc,#8c6a5a 60%,#3e3e48)}
.ph-care{background:linear-gradient(160deg,#c9c1a8,#b58a6e 55%,#6f6a5a)}
.ph-kid{background:linear-gradient(160deg,#eaded0,#c8a07e 55%,#3a5e8a)}
.ph-city{background:linear-gradient(180deg,#9fc2dc,#c9a27a 55%,#3c566e)}
.ph-woman{background:linear-gradient(160deg,#efe9e2,#d9c7ae 55%,#e8e3dc)}
.ph-dark{background:linear-gradient(160deg,#6b5c4c,#3b332b)}
.ph-office{background:linear-gradient(160deg,#8c7b6a,#4b4640)}
.ph-senior{background:linear-gradient(160deg,#7a5e4b,#c493c9 55%,#8a6a5a)}
.ph-forest{background:linear-gradient(180deg,#707a4a,#3e4a2e)}
.ph-road{background:linear-gradient(160deg,#55606a,#2e3338)}
.ph-nurse{background:linear-gradient(160deg,#d7e3ea,#7a9ab0)}
.sea{background:linear-gradient(180deg,#6db8e0,#2a7db8)}
.heath{background:linear-gradient(180deg,#4f7a34 0%,#6b8f45 40%,var(--heath-a) 75%,#8aa35a)}
.slide{position:absolute;top:0;height:134px;border-radius:4px;overflow:hidden}
.slide-cap{position:absolute;inset:0;display:flex;flex-direction:column;align-items:center;justify-content:center;color:var(--white);text-align:center;background:rgba(0,0,0,.35)}
.slide-cap b{font-size:7px;margin-bottom:6px}
.slide-cap .small{color:#eee;width:90px}
.arrow{position:absolute;top:60px;width:0;height:0;border-top:6px solid transparent;border-bottom:6px solid transparent}
.list{list-style:none;font-size:4px;line-height:11px;color:var(--white)}
.list li::before{content:"•";margin-right:5px}
.wave{position:absolute;left:0;width:100%}
.footer{position:absolute;left:0;bottom:0;width:100%;height:87px;background:linear-gradient(180deg,var(--blue-light),var(--blue))}
</style>
</head>
<body>
<div class="stage">

  <!-- Startseite -->
  <section class="page page--home">
    <header class="header">
      <div class="brand" style="left:28px;top:20px"><i></i>Taleb Pflegedienst</div>
      <nav class="nav" style="left:148px"><span>Über Taleb</span><span>Leistungen</span><span>Leitbild</span><span>Geschichten</span><span>Jobs</span></nav>
      <div class="nav-cta" style="left:360px;width:84px">Kontakt</div>
    </header>

    <div class="hero">
      <div class="hero-photo heath" role="img" aria-label="Heidelandschaft mit Weg und Bank"></div>
      <div class="hero-stripe"></div>
      <h1 style="top:58px">IN SEINER EINZIGARTIGKEIT</h1>
      <h2 style="top:96px">STEHT DER MENSCH<br>IM MITTELPUNKT</h2>
    </div>

    <div class="band" style="top:250px;height:105px">
      <h3>Ihr ambulanter Intensivpflegedienst</h3>
      <div class="rule"></div>
      <p class="small">Wir begleiten Menschen zu Hause und unterwegs, mit festen Teams und viel Zeit für das, was wirklich zählt im Alltag.</p>
    </div>
    <div class="card" style="left:57px;top:330px;width:105px;height:62px"><b>KINDER</b><p class="small">Liebevolle Betreuung für die Kleinsten, ganz nah an der Familie und im Alltag.</p></div>
    <div class="card" style="left:170px;top:330px;width:105px;height:62px"><b>JUGENDLICHE</b><p class="small">Begleitung in Schule, Freizeit und Ausbildung mit festen Bezugspersonen.</p></div>
    <div class="card" style="left:283px;top:330px;width:105px;height:62px"><b>ERWACHSENE</b><p class="small">Selbstbestimmtes Leben daheim, im Beruf oder an der Uni mit Sicherheit.</p></div>

    <div class="photo ph-heath" style="left:57px;top:448px;width:85px;height:72px" role="img" aria-label="Heide im Abendlicht"></div>
    <div class="photo ph-team" style="left:85px;top:500px;width:136px;height:106px" role="img" aria-label="Gruppenfoto des Pflegeteams"></div>
    <div class="abs" style="left:254px;top:478px;width:140px">
      <p class="eyebrow">Über uns</p>
      <p class="h4">Wir von Taleb</p>
      <p class="small">Seit über zwanzig Jahren sind wir für unsere Kundinnen und Kunden da. Unser Team ist klein, herzlich und erfahren, viele Kolleginnen arbeiten schon lange bei uns. Wir nehmen uns Zeit, hören zu und gestalten die Pflege gemeinsam mit den Familien.</p>
    </div>
    <div class="btn" style="left:254px;top:565px">Mehr erfahren</div>

    <svg class="wave" style="top:650px" width="444" height="270" viewBox="0 0 444 270" preserveAspectRatio="none" aria-hidden="true">
      <path d="M0 20 C60 0 110 40 180 20 S300 0 360 20 S420 40 444 20 V270 H0Z" fill="#e3f3fc"/>
      <path d="M330 10 Q390 0 444 20 V270 H190Z" fill="#5cc8f6"/>
    </svg>
    <div class="abs" style="left:57px;top:700px;width:140px">
      <p class="eyebrow">Pflegeleistungen</p>
      <p class="h4">Von Mensch zu Mensch</p>
      <p class="small">Unsere Pflegefachkräfte sind dauerhaft vor Ort und kennen die Wünsche ihrer Kundinnen genau. So entsteht Vertrauen, Ruhe und Sicherheit im eigenen Zuhause.<br><br>Wir planen jeden Einsatz individuell, stimmen uns mit Ärzten und Therapeuten ab und sorgen dafür, dass Schule, Studium, Arbeit und Freizeit möglich bleiben. Auch unterwegs begleiten wir zuverlässig.</p>
    </div>
    <div class="btn" style="left:57px;top:860px">Mehr erfahren</div>
    <div class="abs" style="left:310px;top:748px">
      <p style="font-size:9px;font-weight:500;color:var(--white);margin-bottom:4px">Leistungen</p>
      <ul class="list" style="border-left:1px solid rgba(255,255,255,.6);padding-left:8px">
        <li>Intensivpflege zu Hause</li><li>Beatmung und Überwachung</li><li>Begleitung in Schule</li><li>Begleitung im Studium</li><li>Freizeit und Reisen</li><li>Beratung der Angehörigen</li>
      </ul>
    </div>

    <div class="band" style="top:910px;height:210px">
      <p style="font-size:4px;margin-top:26px;letter-spacing:.3px">LEITBILD &amp; WERTE</p>
      <h3 style="margin-top:2px">Seit 20 Jahren persönlich da</h3>
      <div class="rule"></div>
      <p class="small">Verlässlichkeit, Respekt und Herzlichkeit prägen unsere Arbeit jeden Tag, bei jedem Einsatz.</p>
    </div>
    <div class="card" style="left:57px;top:1010px;width:105px;height:106px"><svg class="icon" width="16" height="16" viewBox="0 0 16 16"><circle cx="8" cy="6" r="4" fill="none" stroke="#e293d8"/><path d="M3 14h10" stroke="#e293d8"/></svg><b>STÄNDIGE<br>WEITERBILDUNG</b><p class="small">Regelmäßige Schulungen halten unser Wissen aktuell und sicher.</p></div>
    <div class="card" style="left:170px;top:1010px;width:105px;height:106px"><svg class="icon" width="16" height="16" viewBox="0 0 16 16"><circle cx="5" cy="6" r="2" fill="none" stroke="#e293d8"/><circle cx="11" cy="6" r="2" fill="none" stroke="#e293d8"/><path d="M1 14q4-6 7 0q3-6 7 0" fill="none" stroke="#e293d8"/></svg><b>GUTE<br>KOMMUNIKATION</b><p class="small">Offener Austausch mit Familien, Ärzten und im ganzen Team.</p></div>
    <div class="card" style="left:283px;top:1010px;width:105px;height:106px"><svg class="icon" width="16" height="16" viewBox="0 0 16 16"><path d="M8 14L2 8a3 3 0 0 1 6-4a3 3 0 0 1 6 4z" fill="none" stroke="#e293d8"/></svg><b>WÜRDE, RESPEKT<br>&amp; VERTRAUEN</b><p class="small">Jeder Mensch wird so begleitet, wie er es sich wünscht.</p></div>
    <div class="btn" style="left:190px;top:1133px">Mehr erfahren</div>

    <svg class="wave" style="top:1170px" width="444" height="40" viewBox="0 0 444 40" preserveAspectRatio="none" aria-hidden="true"><path d="M0 10 C80 30 160 0 240 15 S380 30 444 10 V40 H0Z" fill="#e3f3fc"/></svg>
    <div class="abs" style="left:57px;top:1210px;width:300px">
      <p class="eyebrow eyebrow--pink">Ganz nah am Menschen</p>
      <p class="h4">Besondere Geschichten</p>
      <p class="small" style="width:190px">Unsere Kundinnen und Kunden sind aktiv, mobil und engagiert. Hier erzählen sie, was sie bewegt und was sie gemeinsam mit uns erleben.</p>
    </div>
    <div class="btn" style="left:325px;top:1260px">Mehr erfahren</div>
    <div class="abs" style="left:0;top:1292px;width:444px;height:134px">
      <div class="slide ph-kid" style="left:0;width:134px" role="img" aria-label="Lachender Junge im Rollstuhl"></div>
      <div class="slide ph-dark" style="left:141px;width:162px" role="img" aria-label="E-Rolli-Fußball in der Halle"><div class="slide-cap"><b>E-ROLLI-FUSSBALL IN<br>BARMSTEDT</b><p class="small">Jeden Samstag trifft sich das Team zum Training in der Halle.</p></div></div>
      <div class="slide ph-office" style="left:310px;width:134px" role="img" aria-label="Junge Frau am Arbeitsplatz mit Bildschirm"></div>
      <div class="arrow" style="left:44px;border-right:9px solid #fff"></div>
      <div class="arrow" style="left:388px;border-left:9px solid #fff"></div>
    </div>

    <div class="abs" style="left:57px;top:1515px;width:140px">
      <p class="eyebrow">Jobs</p>
      <p class="h4" style="line-height:14px">Bewerben Sie<br>sich bei uns!</p>
      <p class="small">Wir suchen Pflegefachkräfte, die mit Herz arbeiten. Bei uns erwarten Sie feste Teams, faire Bezahlung und viel Wertschätzung im Alltag.</p>
    </div>
    <div class="btn" style="left:57px;top:1618px">Mehr erfahren</div>
    <div class="photo ph-city" style="left:226px;top:1488px;width:106px;height:94px" role="img" aria-label="Hafenstadt mit Blick aufs Wasser"></div>
    <div class="photo ph-woman" style="left:281px;top:1538px;width:106px;height:125px" role="img" aria-label="Lächelnde Frau am Telefon"></div>

    <div class="abs heath" style="left:0;top:1725px;width:444px;height:200px;background:linear-gradient(180deg,#6a6f55,#4a4f3a)" role="img" aria-label="Zwei Hände halten sich"></div>
    <div class="card" style="left:113px;top:1757px;width:218px;height:128px;padding:12px 14px 0">
      <svg class="icon" width="22" height="14" viewBox="0 0 22 14"><rect x="1" y="1" width="20" height="12" fill="none" stroke="#e293d8"/><path d="M1 1l10 7 10-7" fill="none" stroke="#e293d8"/></svg>
      <b style="font-size:13px;font-weight:500">Nehmen Sie Kontakt auf</b>
      <p class="small" style="width:170px">Wir freuen uns auf Ihre Nachricht und rufen gerne zurück. Gemeinsam finden wir die passende Versorgung für Sie.</p>
      <div style="display:flex;justify-content:space-between;text-align:left;margin-top:10px;font-size:4px;line-height:6.5px">
        <p><b style="font-size:4px;display:inline;margin:0">Taleb Pflegedienst</b><br>Lindenweg 12<br>21200 Musterstadt</p>
        <p style="color:var(--blue)">Tel. 040 / 12 3456 789<br>info@taleb-pflegedienst.de</p>
      </div>
    </div>
    <svg class="wave" style="top:1905px" width="444" height="30" viewBox="0 0 444 30" preserveAspectRatio="none" aria-hidden="true"><path d="M0 12 C100 0 200 30 300 12 S420 5 444 12 V30 H0Z" fill="#5cc8f6"/></svg>
    <footer class="footer" style="height:80px;bottom:7px">
      <div class="brand" style="left:50px;top:28px;color:var(--white);font-size:12px"><i style="background:var(--white)"></i>Taleb Pflegedienst</div>
      <p class="abs" style="left:240px;top:26px;font-size:4px;line-height:6.5px;color:var(--white)">Impressum<br>AGB<br>Datenschutz</p>
      <p class="abs" style="left:345px;top:26px;font-size:4px;line-height:6.5px;color:var(--white)">Taleb Pflegedienst<br>Lindenweg 12<br>21200 Musterstadt</p>
    </footer>
    <div class="abs" style="left:0;bottom:0;width:444px;height:7px;background:var(--dark)"></div>
  </section>

  <!-- Leistungen -->
  <section class="page page--services">
    <header class="header">
      <nav class="nav" style="left:0"><span>Über Taleb</span><span>Leistungen</span><span>Leitbild</span><span>Geschichten</span><span>Jobs</span><span>Kontakt</span></nav>
      <div class="nav-cta" style="left:318px;width:127px;padding-right:14px;font-size:8px">Taleb Pflegedienst</div>
    </header>
    <div class="hero">
      <div class="hero-photo ph-senior" style="clip-path:polygon(88% 0,100% 0,100% 100%,55% 100%)" role="img" aria-label="Ältere Dame mit junger Begleiterin beim Kaffee"></div>
      <div class="hero-stripe"></div>
      <h1 style="left:60px;top:58px">UNSERE LEISTUNGEN</h1>
      <h2 style="left:60px;top:96px">FÜR SEHR BESONDERE<br>MENSCHEN</h2>
    </div>
    <div class="band" style="top:250px;height:105px">
      <h3 style="margin-left:60px">Nähe aus Leidenschaft</h3>
      <div class="rule" style="margin-left:calc(50% + 19px)"></div>
      <p class="small" style="margin-left:calc(50% - 65px)">Wir arbeiten mit Herz und Verstand, damit unsere Kundinnen ein selbstbestimmtes Leben führen. Jeder Einsatz wird individuell geplant und gemeinsam mit den Familien gestaltet.</p>
    </div>
    <div class="photo ph-care" style="left:58px;top:396px;width:108px;height:124px" role="img" aria-label="Seniorin beim gemeinsamen Kochen"></div>
    <div class="photo ph-kid" style="left:112px;top:487px;width:108px;height:94px" role="img" aria-label="Mädchen mit Büchern in der Schule"></div>
    <div class="abs" style="left:255px;top:424px;width:140px">
      <p class="eyebrow">Ganz nah an unseren Kunden</p>
      <p class="h4">Echtes Interesse</p>
      <p class="small">Wir lernen unsere Kundinnen kennen, bevor die Pflege beginnt. So wissen wir, was ihnen wichtig ist, welche Routinen sie mögen und wie wir den Alltag gut begleiten.<br><br>Feste Teams sorgen für Vertrauen und Ruhe. Angehörige werden einbezogen und jederzeit gut informiert.</p>
    </div>
    <svg class="wave" style="top:645px" width="445" height="520" viewBox="0 0 445 520" preserveAspectRatio="none" aria-hidden="true">
      <defs><linearGradient id="svcBlue" x1="0" y1="0" x2="0" y2="1"><stop offset="0" stop-color="#2aa6e6"/><stop offset="1" stop-color="#1b6aa3"/></linearGradient></defs>
      <path d="M0 20 C80 0 150 30 230 15 S380 0 445 25 V495 C360 520 280 480 200 500 S60 515 0 495Z" fill="url(#svcBlue)"/>
    </svg>
    <div class="abs" style="left:0;top:685px;width:445px;text-align:center;color:var(--white)">
      <p style="font-size:4px;letter-spacing:.3px">FÜR UNS SELBSTVERSTÄNDLICH</p>
      <p style="font-size:13px;font-weight:700;margin:2px 0 6px">Unser Pflegeservice</p>
      <div class="rule"></div>
      <p class="small" style="color:#e3f3fc;width:190px;margin:0 auto">Diese Werte begleiten uns in jedem Einsatz und in jeder Begegnung mit Menschen.</p>
    </div>
    <div class="card" style="left:20px;top:770px;width:105px;height:106px"><svg class="icon" width="16" height="16" viewBox="0 0 16 16"><circle cx="8" cy="6" r="4" fill="none" stroke="#555"/><path d="M3 14h10" stroke="#555"/></svg><b>STÄNDIGE<br>WEITERBILDUNG</b><p class="small">Regelmäßige Schulungen halten unser Wissen aktuell und sicher.</p></div>
    <div class="card" style="left:132px;top:770px;width:105px;height:106px"><svg class="icon" width="16" height="16" viewBox="0 0 16 16"><circle cx="5" cy="6" r="2" fill="none" stroke="#555"/><circle cx="11" cy="6" r="2" fill="none" stroke="#555"/><path d="M1 14q4-6 7 0q3-6 7 0" fill="none" stroke="#555"/></svg><b>GUTE<br>KOMMUNIKATION</b><p class="small">Offener Austausch mit Familien, Ärzten und im ganzen Team.</p></div>
    <div class="card" style="left:245px;top:770px;width:105px;height:106px"><svg class="icon" width="16" height="16" viewBox="0 0 16 16"><path d="M8 14L2 8a3 3 0 0 1 6-4a3 3 0 0 1 6 4z" fill="none" stroke="#555"/></svg><b>WÜRDE, RESPEKT<br>&amp; VERTRAUEN</b><p class="small">Jeder Mensch wird so begleitet, wie er es sich wünscht.</p></div>
    <div class="card" style="left:20px;top:885px;width:105px;height:106px"><svg class="icon" width="16" height="16" viewBox="0 0 16 16"><circle cx="8" cy="6" r="4" fill="none" stroke="#555"/><path d="M3 14h10" stroke="#555"/></svg><b>STÄNDIGE<br>WEITERBILDUNG</b><p class="small">Regelmäßige Schulungen halten unser Wissen aktuell und sicher.</p></div>
    <div class="card" style="left:132px;top:885px;width:105px;height:106px"><svg class="icon" width="16" height="16" viewBox="0 0 16 16"><circle cx="5" cy="6" r="2" fill="none" stroke="#555"/><circle cx="11" cy="6" r="2" fill="none" stroke="#555"/><path d="M1 14q4-6 7 0q3-6 7 0" fill="none" stroke="#555"/></svg><b>GUTE<br>KOMMUNIKATION</b><p class="small">Offener Austausch mit Familien, Ärzten und im ganzen Team.</p></div>
    <div class="card" style="left:245px;top:885px;width:105px;height:106px"><svg class="icon" width="16" height="16" viewBox="0 0 16 16"><path d="M8 14L2 8a3 3 0 0 1 6-4a3 3 0 0 1 6 4z" fill="none" stroke="#555"/></svg><b>WÜRDE, RESPEKT<br>&amp; VERTRAUEN</b><p class="small">Jeder Mensch wird so begleitet, wie er es sich wünscht.</p></div>
    <div class="card" style="left:20px;top:1000px;width:105px;height:106px"><svg class="icon" width="16" height="16" viewBox="0 0 16 16"><circle cx="8" cy="6" r="4" fill="none" stroke="#555"/><path d="M3 14h10" stroke="#555"/></svg><b>STÄNDIGE<br>WEITERBILDUNG</b><p class="small">Regelmäßige Schulungen halten unser Wissen aktuell und sicher.</p></div>
    <div class="card" style="left:132px;top:1000px;width:105px;height:106px"><svg class="icon" width="16" height="16" viewBox="0 0 16 16"><circle cx="5" cy="6" r="2" fill="none" stroke="#555"/><circle cx="11" cy="6" r="2" fill="none" stroke="#555"/><path d="M1 14q4-6 7 0q3-6 7 0" fill="none" stroke="#555"/></svg><b>GUTE<br>KOMMUNIKATION</b><p class="small">Offener Austausch mit Familien, Ärzten und im ganzen Team.</p></div>
    <div class="card" style="left:245px;top:1000px;width:105px;height:106px"><svg class="icon" width="16" height="16" viewBox="0 0 16 16"><path d="M8 14L2 8a3 3 0 0 1 6-4a3 3 0 0 1 6 4z" fill="none" stroke="#555"/></svg><b>WÜRDE, RESPEKT<br>&amp; VERTRAUEN</b><p class="small">Jeder Mensch wird so begleitet, wie er es sich wünscht.</p></div>

    <div class="abs" style="left:0;top:1196px;width:445px;text-align:center">
      <p class="eyebrow eyebrow--pink">Ganz nah am Menschen</p>
      <p class="h4" style="margin-top:2px">Besondere Angebote</p>
      <div class="rule" style="background:var(--pink)"></div>
      <p class="small" style="width:190px;margin:0 auto">Ausflüge, Reisen und gemeinsame Erlebnisse gehören für uns selbstverständlich zur Pflege dazu, ganz nach den Wünschen unserer Kundinnen.</p>
    </div>
    <div class="abs" style="left:0;top:1282px;width:445px;height:134px">
      <div class="slide ph-road" style="left:0;width:96px" role="img" aria-label="Rollstuhlgerechter Transporter"></div>
      <div class="slide ph-office" style="left:103px;width:162px" role="img" aria-label="Zimmer einer Ferienunterkunft"><div class="slide-cap"><b>ERHOLSAMEN URLAUB<br>BAD BEVENSEN</b><p class="small">Gemeinsam verreisen und neue Kraft tanken in ruhiger Umgebung.</p></div></div>
      <div class="slide ph-nurse" style="left:272px;width:173px" role="img" aria-label="Junge Frau bei einer Untersuchung"></div>
      <div class="arrow" style="left:10px;border-right:9px solid #fff"></div>
      <div class="arrow" style="left:350px;border-left:9px solid #fff"></div>
    </div>
    <svg class="wave" style="top:1455px" width="445" height="250" viewBox="0 0 445 250" preserveAspectRatio="none" aria-hidden="true">
      <path d="M0 20 C60 0 110 40 180 20 S300 0 360 20 S420 40 445 20 V250 H0Z" fill="#e3f3fc"/>
      <path d="M260 10 Q360 0 445 20 V250 H140Z" fill="#5cc8f6"/>
    </svg>
    <div class="abs" style="left:20px;top:1515px;width:110px">
      <p class="eyebrow">Pflegeleistungen</p>
      <p class="h4">Lorem Ipsum</p>
      <p class="small">Wir begleiten Menschen mit hohem Pflegebedarf rund um die Uhr. Unsere Fachkräfte sind gut ausgebildet, arbeiten in festen Teams und kennen jede Besonderheit.<br><br>So bleibt das Leben zu Hause sicher, vertraut und voller Möglichkeiten.</p>
    </div>
    <div class="abs" style="left:255px;top:1528px">
      <p style="font-size:9px;font-weight:500;color:var(--white);margin-bottom:4px">Aufzählung</p>
      <ul class="list" style="border-left:1px solid rgba(255,255,255,.6);padding-left:8px">
        <li>Pflege rund um die Uhr</li><li>Feste Bezugspersonen</li><li>Begleitung im Alltag</li><li>Fahrten und Ausflüge</li><li>Beratung der Familie</li><li>Schule und Studium</li><li>Urlaub und Reisen</li><li>Therapie vor Ort</li>
      </ul>
    </div>
    <div class="abs" style="left:0;bottom:0;width:445px;height:20px;background:var(--dark)"></div>
  </section>

</div>
</body>
</html>
```